Staffing Company Website

We need a website for a new company based out of central California called "Harvest Lane Staffing". We staff truck drivers for agriculture trucking businesses. We don't want a super corporate feel, we want something that feels more inviting to the kind of person who would work in Agriculture/Trucking while still being professional. Please let me know if you have any questions

```html
<!DOCTYPE html>
<html lang="en">
<head>
<meta charset="utf-8">
<title>Harvest Lane Staffing</title>
<link rel="stylesheet" href="https://fonts.googleapis.com/css2?family=Outfit:wght@400;500;600;700&family=Poppins:wght@400;500&display=swap">
<style>
:root{
  --green:#0aa83f;
  --dark:#2c343c;
  --ink:#111;
  --soft:#f3f3f3;
  --white:#fff;
  --text:#222;
}
*{box-sizing:border-box;margin:0;padding:0}
html,body{width:1200px;height:3849px;overflow:hidden}
body{position:relative;background:var(--white);font-family:"Outfit",sans-serif;color:var(--text)}
.abs{position:absolute}
.brand{display:flex;align-items:center;gap:14px;font-weight:600;color:var(--dark);text-transform:uppercase}
.brand-mark{width:60px;height:60px;background:var(--dark);border-radius:8px}
.brand-name{line-height:1.15}
.site-header{left:0;top:0;width:1200px;height:103px;background:var(--white)}
.site-header .brand{left:72px;top:12px;font-size:19px}
.main-nav{right:65px;top:40px;display:flex;gap:35px;font-size:13px;color:var(--ink);font-family:"Poppins",sans-serif}
.photo{display:block}
.hero-photo{left:0;top:103px;width:1200px;height:640px;background:linear-gradient(180deg,#c9d3d8 0%,#d8dde0 35%,#c7a55a 55%,#b58e3e 100%)}
.hero-truck{left:600px;top:260px;width:600px;height:250px;background:linear-gradient(90deg,#b7b9b8,#8b9a8e 70%,#3b6b3a);border-radius:10px;opacity:.75}
.hero-card{left:67px;top:166px;width:550px;height:378px;background:rgba(235,236,238,.88);border-radius:40px}
.hero-card h1{position:absolute;left:60px;top:50px;font-size:57px;line-height:1.15;font-weight:600;color:var(--ink)}
.hero-card p{position:absolute;left:66px;top:183px;width:420px;font-size:17.5px;line-height:1.5;color:var(--ink)}
.btn{position:absolute;display:flex;align-items:center;justify-content:center;background:var(--dark);color:var(--white);border-radius:6px 22px 6px 22px;font-weight:500;text-transform:uppercase;letter-spacing:.3px}
.btn::before{content:"";position:absolute;left:-7px;top:-7px;width:100%;height:60%;border-top:7px solid var(--green);border-left:7px solid var(--green);border-radius:24px 0 0 0;z-index:-1}
.btn{z-index:1}
.btn-black{background:#000}
.wave{left:0;width:1200px}
.eyebrow{font-size:20px;color:var(--green);display:flex;align-items:center;gap:8px}
.eyebrow .line{display:inline-block;width:76px;height:3px;background:var(--green)}
.section-title{font-size:50px;font-weight:600;color:var(--ink);line-height:1}
.service-card{top:971px;width:336px;height:377px;border-radius:34px 0 34px 0;overflow:hidden;background:linear-gradient(160deg,#5d6a78,#9fb0bf 55%,#3a4450)}
.service-card .label{position:absolute;left:0;bottom:0;width:100%;height:78px;background:rgba(40,40,40,.78);color:var(--white);font-size:24px;font-weight:500;display:flex;align-items:center;justify-content:center}
.about-text{left:133px;top:1733px;width:467px;font-size:14.5px;line-height:28px;color:var(--ink)}
.frame{border:2px solid var(--green)}
.cta-band{left:0;top:2141px;width:1200px;height:521px;background:var(--soft)}
.cta-photo{left:0;top:2141px;width:760px;height:521px;background:linear-gradient(90deg,#6a8d3e 0%,#8fb04f 45%,#cbd7b7 75%,rgba(243,243,243,0) 100%)}
.cta-title{left:527px;top:2272px;font-size:51px;line-height:72px;font-weight:500;color:var(--ink)}
.field{position:absolute;background:var(--white);box-shadow:0 2px 8px rgba(0,0,0,.12);font-family:"Poppins",sans-serif;font-size:11px;color:#888;padding:12px 18px}
.footer-bg{left:0;top:3300px;width:1200px;height:490px;background:var(--soft)}
.contact-item{display:flex;align-items:center;gap:14px;font-size:14px;color:var(--ink);line-height:1.3;font-family:"Poppins",sans-serif}
.contact-item .ico{width:30px;height:30px;background:#000;border-radius:5px;display:flex;align-items:center;justify-content:center}
.footer-nav{left:0;top:3730px;width:1200px;display:flex;justify-content:center;gap:52px;font-size:14px;color:var(--ink);font-family:"Poppins",sans-serif}
.footer-rule{left:69px;top:3705px;width:1066px;height:1px;background:#bbb}
.bottom-bar{left:0;top:3790px;width:1200px;height:59px;background:#000;color:var(--white);font-size:12px;font-family:"Poppins",sans-serif}
.bottom-bar .copy{position:absolute;left:69px;top:21px}
.social{position:absolute;right:65px;top:15px;display:flex;gap:5px}
.social span{width:28px;height:28px;border:1.5px solid var(--white);border-radius:4px}
</style>
</head>
<body>

<header class="site-header abs">
  <div class="brand abs"><span class="brand-mark"></span><span class="brand-name">Harvest Lane<br>Staffing</span></div>
  <nav class="main-nav abs"><span>HOME</span><span>ABOUT US</span><span>SERVICES</span><span>WHY CHOOSE US?</span><span>TESTIMONIALS</span><span>CONTACT US</span></nav>
</header>

<div class="hero-photo abs photo" role="img" aria-label="Tractor pulling a grain trailer across a golden wheat field"></div>
<div class="hero-truck abs" role="img" aria-label="Tractor and trailer"></div>
<svg class="wave abs" style="top:560px" width="1200" height="200" viewBox="0 0 1200 200">
  <path d="M0 110 C120 20 300 30 470 70 C650 110 700 190 850 180 C1000 170 1120 120 1200 80 L1200 200 L0 200Z" fill="#fff"/>
  <path d="M0 110 C120 20 300 30 470 70 C650 110 700 190 850 180 C1000 170 1120 120 1200 80" fill="none" stroke="var(--green)" stroke-width="14"/>
</svg>
<div class="hero-card abs">
  <h1>HARVEST LANE<br>STAFFING</h1>
  <p>Lorem ipsum dolor sit amet, consectetur adipiscing elit, sed do eiusmod tempor incididunt ut labore et</p>
  <a class="btn" style="left:64px;top:257px;width:223px;height:72px;font-size:18px">Apply&nbsp; Now</a>
</div>

<div class="eyebrow abs" style="left:460px;top:821px"><span class="line"></span>What We Do<span class="line"></span></div>
<h2 class="section-title abs" style="left:0;width:1200px;text-align:center;top:855px">OUR SERVICES</h2>
<div class="service-card abs" style="left:72px" role="img" aria-label="Smiling truck driver at the wheel"><div class="label">Service Name 1</div></div>
<div class="service-card abs" style="left:435px;background:linear-gradient(160deg,#1f3aa8,#6d8fd6 55%,#22306e)" role="img" aria-label="Driver leaning out of a blue truck cab"><div class="label">Service Name 2</div></div>
<div class="service-card abs" style="left:796px" role="img" aria-label="Driver steering a large truck"><div class="label">Service Name 3</div></div>
<a class="btn" style="left:496px;top:1434px;width:215px;height:66px;font-size:17px">View More</a>

<div class="eyebrow abs" style="left:133px;top:1638px">Who We Are<span class="line"></span></div>
<h2 class="section-title abs" style="left:133px;top:1668px">ABOUT US</h2>
<p class="about-text abs">Lorem ipsum dolor sit amet, consectetur adipiscing elit, sed do eiusmod tempor incididunt ut labore et dolore magna aliqua. Ut enim ad minim veniam, quis nostrud exercitation ullamco laboris nisi ut aliquip ex ea commodo consequat. Duis aute irure dolor in reprehenderit in voluptate velit esse cillum dolore eu fugiat nulla pariatur. Excepteur sint occaecat cupidatat non proident, sunt in culpa qui officia deserunt mollit anim id est laborum.</p>
<a class="btn" style="left:141px;top:1962px;width:171px;height:52px;font-size:14px">Read More</a>
<div class="abs photo" style="left:662px;top:1643px;width:388px;height:364px;background:linear-gradient(180deg,#9cc3e6 0%,#c7dbe9 40%,#2f7a3a 65%,#1e4f27 100%)" role="img" aria-label="Farm workers on a green combine harvester"></div>
<div class="frame abs" style="left:678px;top:1628px;width:388px;height:364px"></div>

<div class="cta-band abs"></div>
<div class="cta-photo abs photo" role="img" aria-label="Red tractor on a green grass field at sunset"></div>
<div class="eyebrow abs" style="left:530px;top:2243px">Harvest Lane Staffing<span class="line"></span></div>
<h2 class="cta-title abs">Are You Looking For Truck<br>Drivers For Agriculture<br>Trucking Businesses</h2>
<a class="btn btn-black" style="left:540px;top:2507px;width:214px;height:66px;font-size:25px;font-weight:600">Apply&nbsp; Now</a>

<div class="eyebrow abs" style="left:151px;top:2781px">Get in touch with<span class="line"></span></div>
<h2 class="section-title abs" style="left:151px;top:2812px">CONTACT US</h2>
<div class="field" style="left:154px;top:2907px;width:197px;height:41px">First Name:</div>
<div class="field" style="left:369px;top:2907px;width:199px;height:41px">Last Name:</div>
<div class="field" style="left:154px;top:2966px;width:197px;height:40px">Phone:</div>
<div class="field" style="left:369px;top:2966px;width:199px;height:40px">Email:</div>
<div class="field" style="left:154px;top:3025px;width:414px;height:103px">Mesage:</div>
<a class="btn" style="left:160px;top:3163px;width:170px;height:52px;font-size:14px">Submit Now</a>
<div class="abs photo" style="left:642px;top:2836px;width:389px;height:363px;background:linear-gradient(180deg,#8fb8e0 0%,#cfe0ee 45%,#6cc03a 60%,#b89a5a 85%)" role="img" aria-label="Green combine harvester working a wheat field"></div>
<div class="frame abs" style="left:660px;top:2821px;width:387px;height:363px"></div>

<div class="footer-bg abs"></div>
<svg class="wave abs" style="top:3270px" width="1200" height="180" viewBox="0 0 1200 180">
  <path d="M0 120 C100 40 260 20 420 30 C600 45 680 150 880 160 C1020 165 1130 120 1200 100 L1200 180 L0 180Z" fill="var(--soft)"/>
  <path d="M40 100 C140 40 260 20 420 30 C600 45 680 150 880 160 C1020 165 1130 120 1200 100" fill="none" stroke="var(--green)" stroke-width="13"/>
  <rect x="0" y="0" width="1200" height="30" fill="#fff" opacity="0"/>
</svg>
<div class="brand abs" style="left:466px;top:3482px;font-size:27px;gap:20px"><span class="brand-mark" style="width:90px;height:90px;border-radius:12px"></span><span class="brand-name">Harvest Lane<br>Staffing</span></div>

<div class="contact-item abs" style="left:240px;top:3630px">
  <span class="ico"><svg width="16" height="16" viewBox="0 0 24 24"><path fill="#fff" d="M6.6 10.8a15 15 0 0 0 6.6 6.6l2.2-2.2c.3-.3.7-.4 1-.2 1.1.4 2.3.6 3.6.6.6 0 1 .4 1 1V20c0 .6-.4 1-1 1A17 17 0 0 1 3 4c0-.6.4-1 1-1h3.5c.6 0 1 .4 1 1 0 1.3.2 2.5.6 3.6.1.3 0 .7-.2 1z"/></svg></span>
  <span>CALL US<br>559 010 4821</span></div>
<div class="contact-item abs" style="left:434px;top:3630px">
  <span class="ico"><svg width="16" height="14" viewBox="0 0 24 20"><rect x="1" y="2" width="22" height="16" rx="2" fill="#fff"/><path d="M2 4l10 7 10-7" stroke="#000" stroke-width="2" fill="none"/></svg></span>
  <span>EMAIL US<br>hello@harvestlane.example</span></div>
<div class="contact-item abs" style="left:690px;top:3630px">
  <span class="ico"><svg width="14" height="18" viewBox="0 0 24 30"><path fill="#fff" d="M12 0a10 10 0 0 0-10 10c0 8 10 20 10 20s10-12 10-20A10 10 0 0 0 12 0zm0 14a4 4 0 1 1 0-8 4 4 0 0 1 0 8z"/></svg></span>
  <span>Address line Dummy Here<br>Address line Here</span></div>
<div class="footer-rule abs"></div>
<nav class="footer-nav abs"><span>HOME</span><span>ABOUT US</span><span>SERVICES</span><span>WHY CHOOSE US?</span><span>TESTIMONIALS</span><span>CONTACT US</span></nav>

<footer class="bottom-bar abs">
  <span class="copy">Copyright © 2024 All Rights Reserved By Harvest Lane Staffing</span>
  <div class="social"><span></span><span></span><span></span><span></span></div>
</footer>

</body>
</html>
```